Business Card Design

Lawn service

Industry/Entity Type

Business

Contact Information for Business Card

Fern Hollow Lawn & Garden , deborah finch/owner,operater,2184 wexley millrd.. e. statesboro,ga. 30472, phone:912-555-0147, Residential,Commercial, Lawn and Landscape Maintenance, Bushhogging

```html
<!DOCTYPE html>
<html lang="en">
<head>
<meta charset="utf-8">
<title>Fern Hollow Lawn &amp; Garden — Business Card</title>
<link href="https://fonts.googleapis.com/css2?family=Mulish:wght@400;500;700&display=swap" rel="stylesheet">
<style>
  :root {
    --page-bg: #3a2a22;
    --grass-light: #d4e63a;
    --grass-mid: #8cc63a;
    --grass-deep: #3f8a2c;
    --cream: #fbf9e2;
    --navy: #16174a;
    --leaf-green: #5c8a3c;
    --ink: #1b1b1b;
  }
  * { margin: 0; padding: 0; box-sizing: border-box; }
  html, body { width: 1200px; height: 857px; overflow: hidden; }
  body {
    background: var(--page-bg);
    font-family: "Mulish", "Avenir", sans-serif;
    position: relative;
  }
  .card {
    position: absolute;
    left: 100px; top: 145px;
    width: 1000px; height: 566px;
    overflow: hidden;
    background: var(--cream);
    box-shadow: 0 10px 30px rgba(0,0,0,0.45);
  }
  .grass-field {
    position: absolute; inset: 0 0 150px 0;
    background:
      radial-gradient(ellipse at 20% 30%, var(--grass-light) 0%, rgba(212,230,58,0) 60%),
      linear-gradient(100deg, var(--grass-light) 0%, var(--grass-mid) 40%, var(--grass-deep) 100%);
  }
  .card-shapes { position: absolute; inset: 0; }
  .brand {
    position: absolute; left: 92px; top: 150px; width: 230px;
    text-align: center; color: var(--leaf-green);
  }
  .brand-mark {
    width: 62px; height: 62px; border-radius: 50%;
    background: var(--leaf-green); margin: 0 auto 14px;
  }
  .brand-name { font-size: 30px; font-weight: 700; line-height: 1.1; }
  .brand-sub { font-size: 17px; font-weight: 700; letter-spacing: 5px; margin-top: 2px; }
  .services {
    position: absolute; left: 450px; top: 152px;
    list-style: none; color: var(--ink);
    font-size: 26px; font-weight: 500; line-height: 35px;
  }
  .services li::before { content: "• "; }
  .contact-name {
    position: absolute; right: 635px; top: 415px; text-align: right;
    color: var(--leaf-green);
  }
  .contact-name .person { font-size: 26px; font-weight: 700; text-transform: uppercase; line-height: 1.1; }
  .contact-name .role { font-size: 23px; font-weight: 500; line-height: 1.15; }
  .divider {
    position: absolute; left: 413px; top: 416px; width: 2px; height: 60px;
    background: var(--leaf-green);
  }
  .phone {
    position: absolute; left: 457px; top: 418px;
    font-size: 42px; font-weight: 500; color: var(--leaf-green);
  }
  .address {
    position: absolute; left: 0; right: 0; top: 486px; height: 80px;
    background: var(--navy);
    color: var(--leaf-green);
    font-size: 24px; font-weight: 500; letter-spacing: 4px;
    padding-left: 88px; line-height: 80px;
  }
</style>
</head>
<body>
  <div class="card">
    <div class="grass-field" role="img" aria-label="Close-up photograph of a freshly mown green lawn"></div>
    <svg class="card-shapes" width="1000" height="566" viewBox="0 0 1000 566" aria-hidden="true">
      <path d="M0 361 Q 470 420 1000 361 L1000 566 L0 566 Z" fill="var(--cream)"/>
    </svg>

    <div class="brand">
      <div class="brand-mark"></div>
      <div class="brand-name">Fern Hollow</div>
      <div class="brand-sub">Lawn &amp; Garden</div>
    </div>

    <ul class="services">
      <li>Residential • Commercial</li>
      <li>Lawn and Landscape Maintenance</li>
      <li>Bushhogging</li>
    </ul>

    <div class="contact-name">
      <div class="person">Deborah Finch</div>
      <div class="role">Owner, Operater</div>
    </div>
    <div class="divider"></div>
    <div class="phone">912.555.0147</div>

    <div class="address">2184 Wexley Millrd, E. Statesboro, GA. 30472</div>
  </div>
</body>
</html>
```